Wix web design for healthcare IT consulting firm.

I am looking for a web design built in Wix that it will be easy for me to add or edit content in the future. The web site does not need to be overly complicated, but it should look very polished and professional. I also want to ensure it is mobile device friendly. I do not need any type of on-line purchasing ability. I will eventually do blogs, but for now it is a fairly standard web site with main page, about us, services provided, etc. I would also like a place for potential customers to contact us directly from the web site. I have included a Word document with some content for the web design. I have also included my logo and business card for reference. I would like to utilize similar colors as my business card. One of my primary competitors is https://vonmarlhq.example/

Target Market(s)

Target market could be nursing home CEO, CIO, or other leader at an organization that manages long term care facilities.

Number of Pages Required

5+ page

Colors
876aae

Requirements
Must have
• Be designed to be used in Wix. Use the content I provided to create and make web design. Allow to be viewed on mobile device. Please use similar color structure as attached business card. Please use attached logo in design.

```html
<!DOCTYPE html>
<html lang="en">
<head>
<meta charset="utf-8">
<title>Lumencare Health Solutions</title>
<link rel="stylesheet" href="https://fonts.googleapis.com/css2?family=Open+Sans:wght@300;400;600;700&display=swap">
<style>
:root{
  --purple:#8a5cc9;
  --purple-deep:#7d47c7;
  --purple-soft:#a27dd0;
  --purple-mid:#9461cc;
  --purple-strong:#8a4fd0;
  --text:#333;
  --muted:#8a8a8a;
  --light:#f3f3f3;
  --footer:#ececec;
  --white:#fff;
}
*{box-sizing:border-box;margin:0;padding:0}
html,body{width:1200px;height:2342px;overflow:hidden}
body{font-family:'Open Sans',Arial,sans-serif;color:var(--text);background:var(--white);position:relative}
.abs{position:absolute}
/* header */
.site-header{position:absolute;left:0;top:0;width:1200px;height:75px;background:var(--white);box-shadow:0 1px 4px rgba(0,0,0,.06);z-index:2}
.brand{position:absolute;left:207px;top:14px;display:flex;align-items:center;gap:8px}
.brand-mark{width:14px;height:14px;background:var(--purple)}
.brand-name{font-size:17px;font-weight:700;color:var(--purple);line-height:1.1;letter-spacing:.2px}
.nav{position:absolute;top:27px;font-size:14px;color:#444}
.nav.active{color:var(--purple);font-weight:600}
.nav-cta{position:absolute;left:890px;top:22px;width:142px;height:31px;background:var(--purple);color:var(--white);font-size:14px;text-align:center;line-height:31px}
/* hero */
.hero{position:absolute;left:0;top:75px;width:1200px;height:470px;background:linear-gradient(90deg,#dfe0e2 0%,#e6e6e6 40%,#ddd6bf 62%,#e7dfc4 80%,#d9d2bd 100%)}
.hero-title{position:absolute;left:205px;top:115px;font-size:37px;font-weight:700;color:var(--purple-strong);line-height:1.1}
.hero-sub{position:absolute;left:205px;top:155px;font-size:29px;font-weight:700;color:var(--white);line-height:1.1}
.hero-copy{position:absolute;left:207px;top:202px;width:440px;font-size:14px;line-height:20px;color:var(--white)}
.btn-outline{position:absolute;left:207px;top:338px;width:155px;height:55px;border:3px solid var(--purple);color:var(--purple);font-size:17px;font-weight:600;text-align:center;line-height:49px}
/* section heads */
.eyebrow{position:absolute;font-size:9px;font-weight:600;color:var(--purple);letter-spacing:.4px;text-transform:uppercase}
.section-title{position:absolute;font-size:22px;font-weight:400;color:#222}
/* about */
.about-photo{position:absolute;left:207px;top:664px;width:295px;height:205px;background:linear-gradient(135deg,#c6dce4,#a9c6d1)}
.about-copy{position:absolute;left:553px;top:656px;width:445px;font-size:11px;line-height:20px;color:#777}
/* team */
.team{position:absolute;left:0;top:935px;width:1200px;height:555px;background:var(--light)}
.member-card{position:absolute;left:207px;top:1035px;width:483px;height:400px;background:var(--white);box-shadow:0 2px 6px rgba(0,0,0,.2)}
.member-photo{position:absolute;left:0;top:0;width:483px;height:182px;background:linear-gradient(90deg,#e2e2e2,#bdbdbd 50%,#d8d8d8)}
.member-name{position:absolute;left:21px;top:191px;font-size:14px;font-weight:700;color:var(--purple-strong)}
.member-role{position:absolute;left:21px;top:211px;font-size:9.5px;color:#666}
.member-bio{position:absolute;left:21px;top:231px;width:445px;font-size:9.6px;line-height:14px;color:#777}
/* info cards */
.info-cards{position:absolute;left:207px;top:1633px;width:786px;height:200px;display:flex;box-shadow:0 3px 8px rgba(0,0,0,.25)}
.info-card{flex:1;padding:18px 16px;color:var(--white)}
.info-card:nth-child(1){background:var(--purple-soft)}
.info-card:nth-child(2){background:var(--purple-mid)}
.info-card:nth-child(3){background:var(--purple-strong)}
.info-card h3{font-size:16px;font-weight:400;margin-bottom:8px}
.info-card p{font-size:9.5px;line-height:14px;font-weight:300;height:76px}
.btn-small{display:inline-block;margin-top:18px;border:1px solid var(--white);font-size:10px;padding:3px 8px}
/* mission */
.mission{position:absolute;left:0;top:1920px;width:1200px;height:208px;background:radial-gradient(ellipse at 10% 40%,#dde8f8,transparent 45%),radial-gradient(ellipse at 90% 60%,#dde8f8,transparent 45%),#f7f9fd}
.mission-title{position:absolute;left:0;width:1200px;top:64px;text-align:center;font-size:22px;font-weight:700;color:var(--purple-strong)}
.mission-sub{position:absolute;left:0;width:1200px;top:94px;text-align:center;font-size:15px;color:#333}
.btn-fill{position:absolute;left:524px;top:137px;width:154px;height:46px;background:var(--purple-soft);color:var(--white);font-size:14px;font-weight:600;text-align:center;line-height:46px}
/* footer */
.site-footer{position:absolute;left:0;top:2128px;width:1200px;height:214px;background:var(--footer)}
.foot-head{position:absolute;font-size:14px;font-weight:700;color:var(--purple-strong)}
.foot-list{position:absolute;list-style:none;font-size:10.5px;line-height:22px;color:#777}
.foot-contact{position:absolute;left:800px;top:68px;font-size:10.5px;line-height:22px;color:#777}
.foot-contact span{color:var(--purple-strong)}
.social{position:absolute;top:92px;width:10px;height:10px;border-radius:50%;background:#666}
.legal{position:absolute;left:0;top:2318px;width:1200px;height:24px;border-top:1px solid #ddd;text-align:center;font-size:9.5px;line-height:22px;color:#555;background:var(--footer)}
</style>
</head>
<body>

<header class="site-header">
  <div class="brand"><span class="brand-mark"></span><span class="brand-name">Lumencare<br>Health Solutions</span></div>
  <span class="nav" style="left:506px">Home</span>
  <span class="nav active" style="left:581px">About Us</span>
  <span class="nav" style="left:681px">Services</span>
  <span class="nav" style="left:770px">Contact Us</span>
  <span class="nav-cta">Get Started</span>
</header>

<section class="hero" role="img" aria-label="Close-up photograph of round pale yellow tablets on a light surface">
  <h1 class="hero-title">Increasing the value and security</h1>
  <p class="hero-sub">of your technology resources</p>
  <p class="hero-copy">We understand different organizations have different needs. Lumencare HCS strives to assist your organization by bringing solutions that are easy to understand and allow the customer to track success. We provide solutions based on the customer's needs and desires.</p>
  <span class="btn-outline">Get Started</span>
</section>

<span class="eyebrow" style="left:207px;top:588px">About Us</span>
<h2 class="section-title" style="left:205px;top:598px">Solutions for your needs and desires</h2>
<div class="about-photo" role="img" aria-label="Photograph of a laptop, stethoscope and phone on a pale blue desk"></div>
<p class="about-copy">Lorem ipsum dolor sit amet, consectetur adipiscing elit. Vivamus rhoncus est quis ex ultrices tristique. Sed hendrerit tortor erat, nec elementum massa efficitur varius. Nunc tortor magna, condimentum ac tempor molestie, semper ac magna. Aenean diam dui, consectetur at elit ut, efficitur rutrum libero. Mauris laoreet mollis leo nec commodo. Cras ac nisi dapibus nisi consequat consequat. Cras ornare nibh id turpis ornare, eget auctor dui lacinia. Nullam finibus quam vitae lectus facilisis, eget convallis dui porttitor. Donec pretium id leo nec tempus. Nunc rutrum malesuada ultrices. Mauris non nisl et sem iaculis rhoncus quis at ligula. Vestibulum condimentum tempor rutrum. Maecenas at tristique felis, eu consequat lectus. Vivamus urna lorem, facilisis laoreet congue at, euismod eget est.</p>

<section class="team">
  <span class="eyebrow" style="left:205px;top:25px">Our Team</span>
  <h2 class="section-title" style="left:203px;top:35px">Meet our team</h2>
</section>
<article class="member-card">
  <div class="member-photo" role="img" aria-label="Portrait photograph of the company founder on a grey background"></div>
  <h3 class="member-name">Daniel Reeve</h3>
  <p class="member-role">President and CEO</p>
  <p class="member-bio">As the Founder and CEO of Lumencare HCS, Daniel has been working in the technology industry for over 25 years with extensive experience in healthcare and IT. As a consultant Daniel held multiple roles including CIO and CISO. Over the years, Daniel has been the executive sponsor of multiple electronic health record (EHR) implementations. He has created and nurtured numerous successful IT departments and created strong relationships with leadership teams. Daniel strives to learn and grow as a professional. He holds a Master's in Business Administration as well as a Master's in Healthcare Administration. In addition, Daniel has also achieved certification with both the Council of Health Information Leaders (CHIL) and the Health Systems Technology Society (HSTS).</p>
</article>
<svg class="abs" style="left:735px;top:1216px" width="40" height="40" viewBox="0 0 40 40" aria-label="Next team member">
  <circle cx="20" cy="20" r="20" fill="#8a4fd0"/>
  <path d="M17 12l8 8-8 8" fill="none" stroke="#fff" stroke-width="2.5" stroke-linecap="round" stroke-linejoin="round"/>
</svg>

<span class="eyebrow" style="left:207px;top:1538px">Site Materials</span>
<h2 class="section-title" style="left:207px;top:1549px">Additional information you may like to know</h2>
<div class="info-cards">
  <div class="info-card"><h3>Our Services</h3><p>Lorem ipsum dolor sit amet, consectetur adipiscing elit. Integer eget luctus nisi. Aenean varius ligula ut pellentesque sodales. Sed cursus dictum ullamcorper. Proin felis ipsum, varius ac enim ac, tristique rutrum.</p><span class="btn-small">Read More</span></div>
  <div class="info-card"><h3>Our Team</h3><p>Lorem ipsum dolor sit amet, consectetur adipiscing elit. Integer eget luctus nisi. Aenean varius ligula ut pellentesque sodales. Sed cursus dictum ullamcorper. Proin felis ipsum, varius ac enim ac, tristique rutrum.</p><span class="btn-small">Read More</span></div>
  <div class="info-card"><h3>Contact Us</h3><p>Lorem ipsum dolor sit amet, consectetur adipiscing elit. Integer eget luctus nisi. Aenean varius ligula ut pellentesque sodales. Sed cursus dictum ullamcorper. Proin felis ipsum, varius ac enim ac, tristique rutrum.</p><span class="btn-small">Read More</span></div>
</div>

<section class="mission" role="img" aria-label="Soft blue hexagon pattern background">
  <h2 class="mission-title">OUR MISSION IS TO PARTNER WITH CUSTOMERS</h2>
  <p class="mission-sub">To increase the value of their technology tools</p>
  <span class="btn-fill">Contact Us</span>
</section>

<footer class="site-footer">
  <div class="brand" style="top:30px"><span class="brand-mark"></span><span class="brand-name">Lumencare<br>Health Solutions</span></div>
  <span class="social" style="left:239px"></span>
  <span class="social" style="left:268px"></span>
  <span class="social" style="left:297px"></span>
  <h4 class="foot-head" style="left:437px;top:24px">Our Services</h4>
  <ul class="foot-list" style="left:437px;top:52px">
    <li>Risk Assessment</li><li>Policy Management</li><li>Chief Information Officer</li><li>Chief Information Security Officer</li><li>IT Department Evaluation</li>
  </ul>
  <ul class="foot-list" style="left:632px;top:52px">
    <li>EHR Optimization Services</li><li>EHR Implementation</li><li>EHR Assessment</li><li>EHR Quality Assessment</li><li>EHR Quality Assessment</li>
  </ul>
  <h4 class="foot-head" style="left:800px;top:24px">Contact Us</h4>
  <p class="foot-contact">Email us: <span>dreeve@lumencarehs.example</span><br>Call us: <span>555-014-2290</span></p>
</footer>
<div class="legal">Lumencare Health. All Rights Reserved.</div>

</body>
</html>
```